Advertisement Coaching practice

I need an advertisement (to be printed in newspaper). I have a coaching practice where I offer coaching, workshops family constellations and relationship therapy. The ad needs to express calmness, inspiration to transform but also not dull and boring. It would be great if you could use the colors from my logo into the ad.

Dimensions are: 13,04 cm Width x 9,72 cm Height.

I will add my previous self-made ad, my company logo, a portrait photo of myself and the text I want to add. Also my contact details should be visible as well.

Requirements
Nice to have
• I have updated the brief with a flyer that I had previously made by a designer. It would be a nice to have if the ad ties in with that. You can also look at my website at www.bravemoor.nu to see what colors I used there.

```html
<!DOCTYPE html>
<html lang="nl">
<head>
<meta charset="utf-8">
<title>Bravemoor advertentie</title>
<link href="https://fonts.googleapis.com/css2?family=Montserrat:wght@800&family=Roboto:wght@400;500;700&display=swap" rel="stylesheet">
<style>
  :root {
    --stage: #3a3a3a;
    --teal: #24929a;
    --mint: #8fd3b6;
    --coral: #ef7060;
    --orange: #f6a028;
    --band-gray: #58585a;
    --ink: #555557;
    --white: #ffffff;
    --sand: #fde9c6;
  }
  html, body {
    margin: 0;
    width: 1200px;
    height: 1200px;
    overflow: hidden;
    background: var(--stage);
  }
  .ad {
    position: absolute;
    left: 68px;
    top: 198px;
    width: 1062px;
    height: 804px;
    overflow: hidden;
    background: linear-gradient(90deg, #f3f8f6 0%, #cfe9df 31%, #eef3e2 48%, #fff3da 66%, #fde2b4 90%, #fbc78a 100%);
    box-shadow: 0 10px 30px rgba(0,0,0,.45);
    font-family: "Roboto", Arial, sans-serif;
  }
  .brand {
    position: absolute;
    left: 60px;
    top: 50px;
    width: 212px;
    text-align: center;
    color: var(--ink);
  }
  .brand-mark {
    display: block;
    width: 62px;
    height: 62px;
    margin: 0 auto 12px;
    border: 2px solid #6a6a6c;
    border-radius: 50%;
    box-sizing: border-box;
  }
  .brand-name {
    font-size: 38px;
    font-weight: 400;
    line-height: 1;
    letter-spacing: 1px;
  }
  .headline {
    position: absolute;
    right: 53px;
    top: 40px;
    margin: 0;
    text-align: right;
    font-family: "Montserrat", Arial, sans-serif;
    font-weight: 800;
    font-size: 46px;
    line-height: 50px;
    color: var(--ink);
  }
  .intro-band {
    position: absolute;
    left: 0;
    top: 236px;
    width: 100%;
    height: 83px;
    background: linear-gradient(90deg, var(--band-gray) 0%, #8a8784 20%, var(--band-gray) 34%, var(--band-gray) 100%);
  }
  .intro-text {
    position: absolute;
    right: 53px;
    top: 245px;
    margin: 0;
    text-align: right;
    color: var(--white);
    font-size: 22px;
    line-height: 33px;
  }
  .intro-text strong { font-weight: 700; }
  .offer-band {
    position: absolute;
    left: 0;
    top: 319px;
    width: 100%;
    height: 52px;
    background: linear-gradient(90deg, var(--orange) 0%, #f9c06a 22%, var(--orange) 36%, var(--orange) 100%);
  }
  .offer-title {
    position: absolute;
    right: 53px;
    top: 319px;
    margin: 0;
    line-height: 52px;
    font-size: 30px;
    font-weight: 700;
    letter-spacing: -0.3px;
    color: var(--white);
  }
  .portrait {
    position: absolute;
    left: 4px;
    top: 200px;
    width: 380px;
    height: 420px;
    border-radius: 190px 190px 0 0;
    background: radial-gradient(ellipse at 48% 38%, #b98566 0%, #8b5e46 35%, #c9d2e0 70%, rgba(201,210,224,0) 100%);
  }
  .benefits {
    position: absolute;
    right: 51px;
    top: 376px;
    margin: 0;
    padding: 0;
    list-style: none;
    color: var(--ink);
    font-size: 23px;
    line-height: 30px;
    text-align: right;
  }
  .benefits li {
    display: flex;
    justify-content: flex-end;
    align-items: flex-start;
    gap: 26px;
    margin-bottom: 11px;
  }
  .benefits svg { flex: none; margin-top: -4px; }
  .waves {
    position: absolute;
    left: 0;
    top: 0;
  }
  .about {
    position: absolute;
    left: 53px;
    top: 589px;
    width: 609px;
    margin: 0;
    color: var(--white);
    font-size: 20px;
    line-height: 33px;
    text-align: justify;
  }
  .divider {
    position: absolute;
    left: 727px;
    top: 604px;
    width: 2px;
    height: 146px;
    background: var(--white);
  }
  .contact {
    position: absolute;
    left: 782px;
    top: 604px;
    width: 230px;
    color: var(--white);
  }
  .contact-name {
    margin: 0 0 8px;
    font-size: 25px;
    font-weight: 700;
    text-align: right;
    line-height: 36px;
  }
  .contact-list {
    margin: 0;
    padding: 0;
    list-style: none;
    font-size: 21px;
  }
  .contact-list li {
    display: flex;
    align-items: center;
    gap: 16px;
    height: 38px;
  }
</style>
</head>
<body>
<div class="ad">
  <div class="brand">
    <span class="brand-mark"></span>
    <div class="brand-name">bravemoor</div>
  </div>

  <h1 class="headline">COACHING,<br>FAMILIEOPSTELLINGEN &amp;<br>RELATIETHERAPIE</h1>

  <div class="intro-band"></div>
  <p class="intro-text"><strong>Trauma's en negatieve ervaringen</strong> vormen ons en blijven nog lang<br>voelbaar. Ze kunnen groei of geluk in de weg staan.</p>

  <div class="offer-band"></div>
  <h2 class="offer-title">Ik ben Mirela en ondersteun je bij het:</h2>

  <div class="portrait" role="img" aria-label="Portretfoto van de coach, een glimlachende vrouw met donker opgestoken haar"></div>

  <ul class="benefits">
    <li><span>Doorbreken van belemmerende patronen</span>
      <svg width="38" height="38" viewBox="0 0 38 38"><circle cx="19" cy="19" r="17.5" fill="none" stroke="#555557" stroke-width="1.6"/><path d="M10 15h18M10 22h18M13 12v14M25 12v14" stroke="#555557" stroke-width="1.6" fill="none"/></svg></li>
    <li><span>Beter omgaan met conflicten</span>
      <svg width="38" height="38" viewBox="0 0 38 38"><circle cx="19" cy="19" r="17.5" fill="none" stroke="#555557" stroke-width="1.6"/><path d="M20 10l-5 9h6l-4 9" stroke="#555557" stroke-width="1.6" fill="none"/></svg></li>
    <li><span>In gezonde verbinding met elkaar als koppel of<br>met anderen komen</span>
      <svg width="38" height="38" viewBox="0 0 38 38"><circle cx="19" cy="19" r="17.5" fill="none" stroke="#555557" stroke-width="1.6"/><path d="M19 23c-4-3-6-5-6-7a3 3 0 0 1 6-1 3 3 0 0 1 6 1c0 2-2 4-6 7z M9 24c4 3 16 3 20 0" stroke="#555557" stroke-width="1.6" fill="none"/></svg></li>
  </ul>

  <svg class="waves" width="1062" height="804" viewBox="0 0 1062 804" aria-hidden="true">
    <path d="M585,544 C700,584 840,596 940,566 C995,548 1035,515 1062,470 V522 C1000,562 920,590 820,592 C740,592 660,572 585,544 Z" fill="var(--mint)"/>
    <path d="M0,585 C90,540 200,505 300,500 C200,512 90,550 0,600 Z" fill="var(--coral)"/>
    <path d="M0,600 C150,530 330,500 440,512 C600,530 700,592 820,592 C920,592 1000,562 1062,522 V804 H0 Z" fill="var(--teal)"/>
    <path d="M820,592 C920,592 1000,562 1062,522 V530 C1000,568 920,598 820,598 Z" fill="var(--sand)" opacity=".8"/>
  </svg>

  <p class="about">Maandelijks geef ik workshops familieopstellingen. Ook houd ik themasessies rond adoptie, moeder-dochterdynamiek of relaties. Ook bied ik individuele coaching, relatietherapie en retraites aan. Kijk op de website voor meer info of neem contact op en ontdek wat het beste bij jou past.</p>

  <div class="divider"></div>

  <div class="contact">
    <p class="contact-name">Mirela Dasrath</p>
    <ul class="contact-list">
      <li><svg width="26" height="22" viewBox="0 0 26 22"><rect x="1.5" y="3" width="23" height="16" fill="none" stroke="#fff" stroke-width="1.8"/><path d="M1.5 3l11.5 10L24.5 3M1.5 19l8-7M24.5 19l-8-7" fill="none" stroke="#fff" stroke-width="1.8"/></svg><span>info@bravemoor.nu</span></li>
      <li><svg width="26" height="26" viewBox="0 0 26 26"><path d="M6 2l4 5-2 3c1 3 4 6 7 7l3-2 5 4-2 4C12 23 3 14 2 4z" fill="none" stroke="#fff" stroke-width="1.8"/><path d="M15 6a6 6 0 0 1 5 5M15 2a10 10 0 0 1 9 9" fill="none" stroke="#fff" stroke-width="1.6"/></svg><span>06-12 34 56 78</span></li>
      <li><svg width="26" height="26" viewBox="0 0 26 26"><circle cx="13" cy="13" r="11" fill="none" stroke="#fff" stroke-width="1.8"/><ellipse cx="13" cy="13" rx="5" ry="11" fill="none" stroke="#fff" stroke-width="1.6"/><path d="M2 13h22M4 7h18M4 19h18" stroke="#fff" stroke-width="1.6"/></svg><span>www.bravemoor.nu</span></li>
    </ul>
  </div>
</div>
</body>
</html>
```